Create Design for Business Folders

We need a new design for business folders we will be having printed. The size of the folders are 9X12, and a template can be downloaded from www.pelmarkstudio-example.com. We are using the standard size folders, full color printing on the front only.

Since this is a folder and not a brochure, we do not need a lot of text on the folder. The design is the important issue. It should be bright and colorful enough to take advantage of the full color printing. Branding is important, but this should be easy. Our logo and theme is very common, and there are many stock photos that can be used to create an excellent design.

Basically our theme or branding involves rising color bars indicating a rising credit score. I would like something creative designed around this theme. I do not simply want our logo blown up as the theme. Something highly creative and imaginative is preferred

I would prefer a background that is colorful and covers the entire brochure.

The only thing on the front of the brochure is "Tally Peak Lending" "Lift Every Number, Brighten Every Day"

On the back would be our contact information, with address, phone, web, etc.

Industry/Entity Type

Printing

Font styles to use
Sans Serif

Colors
3276b5
0355a3
ffffff

Requirements
Should not have
• Nothing to dark.

```html
<!DOCTYPE html>
<html lang="en">
<head>
<meta charset="utf-8">
<title>Tally Peak Lending – Business Folder</title>
<link rel="stylesheet" href="https://fonts.googleapis.com/css2?family=Exo+2:wght@300;400;700&display=swap">
<style>
  :root {
    --brand-blue: #3276b5;
    --brand-deep: #0355a3;
    --paper: #ffffff;
    --wave-light: #cfe0f4;
    --wave-mid: #8fb6e2;
    --backdrop: #e6e6e6;
    --ink: #4a5560;
    --photo-top: #dfe6ee;
    --photo-bottom: #7d8c9c;
  }
  * { box-sizing: border-box; margin: 0; padding: 0; }
  html, body { width: 1200px; height: 1000px; overflow: hidden; }
  body {
    background: var(--backdrop);
    font-family: "Exo 2", Arial, sans-serif;
    display: flex;
    align-items: center;
    justify-content: center;
    gap: 60px;
  }
  .folder-panel {
    position: relative;
    width: 420px;
    height: 560px;
    background: var(--paper);
    box-shadow: 0 6px 24px rgba(0,0,0,0.12);
    overflow: hidden;
  }
  .panel-art { position: absolute; inset: 0; width: 100%; height: 100%; }
  .contact-list {
    position: absolute;
    left: 26px;
    bottom: 26px;
    list-style: none;
    font-size: 9px;
    line-height: 1.55;
    color: var(--ink);
  }
  .contact-list li { display: flex; align-items: flex-start; gap: 6px; }
  .contact-list svg { flex: none; width: 9px; height: 9px; margin-top: 2px; fill: var(--brand-blue); }
  .cover-headline {
    position: absolute;
    left: 30px;
    top: 392px;
    font-weight: 300;
    font-size: 19px;
    line-height: 1.25;
    color: var(--ink);
    letter-spacing: 0.3px;
  }
  .brand-lockup {
    position: absolute;
    right: 22px;
    bottom: 26px;
    text-align: right;
  }
  .brand-name {
    display: flex;
    align-items: center;
    justify-content: flex-end;
    gap: 8px;
    font-weight: 700;
    font-size: 20px;
    color: var(--brand-blue);
  }
  .brand-mark { width: 14px; height: 14px; background: var(--brand-blue); }
  .brand-tagline {
    margin-top: 2px;
    font-weight: 700;
    font-size: 7.5px;
    letter-spacing: 0.6px;
    text-transform: uppercase;
    color: var(--brand-deep);
  }
</style>
</head>
<body>

  <!-- Back panel -->
  <section class="folder-panel folder-back" aria-label="Folder back">
    <svg class="panel-art" viewBox="0 0 420 560" aria-hidden="true">
      <defs>
        <linearGradient id="backWave" x1="0" y1="0" x2="1" y2="0">
          <stop offset="0" stop-color="#ffffff" stop-opacity="0"/>
          <stop offset="0.6" stop-color="#8fb6e2"/>
          <stop offset="1" stop-color="#3276b5"/>
        </linearGradient>
      </defs>
      <path d="M0,170 Q180,60 420,20 L420,0 L0,0 Z" fill="#eef4fb"/>
      <path d="M0,200 Q200,70 420,30 L420,55 Q220,95 0,230 Z" fill="url(#backWave)" opacity="0.5"/>
      <path d="M60,170 Q230,60 420,10 L420,22 Q240,70 60,180 Z" fill="url(#backWave)" opacity="0.8"/>
      <path d="M0,140 Q200,40 420,0 L420,6 Q220,50 0,150 Z" fill="#cfe0f4"/>
    </svg>
    <ul class="contact-list">
      <li><svg viewBox="0 0 10 10"><path d="M5 0a3.5 3.5 0 0 0-3.5 3.5C1.5 6 5 10 5 10s3.5-4 3.5-6.5A3.5 3.5 0 0 0 5 0zm0 5a1.5 1.5 0 1 1 0-3 1.5 1.5 0 0 1 0 3z"/></svg><span>4580 Harrow Crest Lane, Suite B2<br>Lindale Park, Ohio 43012</span></li>
      <li><svg viewBox="0 0 10 10"><path d="M2 0l2 2.5-1 1.2a6 6 0 0 0 3.3 3.3l1.2-1L10 8 8.5 10C4 10 0 6 0 1.5z"/></svg><span>(800)555-0148</span></li>
      <li><svg viewBox="0 0 10 10"><rect x="0" y="2" width="10" height="7" rx="1"/></svg><span>(800)555-0192</span></li>
      <li><svg viewBox="0 0 10 10"><path d="M0 2h10v6H0z M0 2l5 3.5L10 2"/></svg><span>hello@tallypeaklending-example.com</span></li>
      <li><svg viewBox="0 0 10 10"><circle cx="5" cy="5" r="5"/></svg><span>www.tallypeaklending-example.com</span></li>
    </ul>
  </section>

  <!-- Front panel -->
  <section class="folder-panel folder-front" aria-label="Folder front">
    <svg class="panel-art" viewBox="0 0 420 560">
      <defs>
        <linearGradient id="frontWave" x1="0" y1="0" x2="1" y2="0">
          <stop offset="0" stop-color="#3276b5"/>
          <stop offset="0.5" stop-color="#8fb6e2"/>
          <stop offset="1" stop-color="#ffffff" stop-opacity="0"/>
        </linearGradient>
        <linearGradient id="lowerWave" x1="0" y1="0" x2="1" y2="0">
          <stop offset="0" stop-color="#ffffff" stop-opacity="0"/>
          <stop offset="0.5" stop-color="#cfe0f4"/>
          <stop offset="1" stop-color="#8fb6e2"/>
        </linearGradient>
        <linearGradient id="photoTone" x1="0" y1="0" x2="0" y2="1">
          <stop offset="0" stop-color="#dfe6ee"/>
          <stop offset="1" stop-color="#7d8c9c"/>
        </linearGradient>
      </defs>
      <g aria-hidden="true">
        <path d="M0,0 L420,0 L420,120 Q210,80 0,110 Z" fill="#eef4fb"/>
        <path d="M0,20 Q200,30 420,75 L420,95 Q200,55 0,50 Z" fill="url(#frontWave)" opacity="0.7"/>
        <path d="M0,5 Q220,10 420,50 L420,60 Q220,25 0,18 Z" fill="url(#frontWave)"/>
      </g>
      <path role="img" aria-label="Photo of a smiling team of business professionals standing in a row"
            d="M0,128 Q210,88 420,128 L420,300 Q300,350 170,345 Q60,340 0,320 Z" fill="url(#photoTone)"/>
      <g aria-hidden="true">
        <path d="M0,320 Q120,350 260,345 Q360,340 420,300 L420,320 Q300,375 150,370 Q60,365 0,340 Z" fill="#eef4fb"/>
        <path d="M0,440 Q200,380 420,420 L420,450 Q220,410 0,470 Z" fill="url(#lowerWave)" opacity="0.8"/>
        <path d="M0,480 Q220,420 420,460 L420,475 Q230,440 0,500 Z" fill="url(#lowerWave)" opacity="0.5"/>
      </g>
    </svg>
    <h1 class="cover-headline">We Legally and Ethically<br>Raise Credit Scores</h1>
    <div class="brand-lockup">
      <div class="brand-name"><span class="brand-mark"></span>Tally Peak Lending</div>
      <p class="brand-tagline">Lift Every Number, Brighten Every Day</p>
    </div>
  </section>

</body>
</html>
```